Thornfield Marsh, LLC Website

We are a small law firm in need of a website that contains the following:
1. Attractive main page
2. About us/attorney info for three people: Leonard Thornfield (attorney), Brent Marsh (attorney), and Melinda Carrow (legal assistant). We have bio's ready to submit.
3. Blog/video page. We'd like to post blogs and videos to help drive traffic
4. Multidistrict Litigation and Class Actions page, where we post information regarding active MDLs and Class actions that we are doing intake on.
Updates

Can you also please use the color "gold" in the design and logo? Thanks.

Industry/Entity Type

Legal

Coding

Coded - Design and coding required

Number of Pages Required

1 page

Colors
0054AA
0677BA
7BADD7
CADEEF
E8F1F8

Requirements
Must have
• 1. Attractive main page 2. About us/attorney info for three people: Leonard Thornfield (attorney), Brent Marsh (attorney), and Melinda Carrow (legal assistant). We have bio's ready to submit. 3. Blog/video page. We'd like to post blogs and videos to help drive traffic 4. Multidistrict Litigation and Class Actions page, where we post information regarding active MDLs and Class actions that we are doing intake on.

```html
<!DOCTYPE html>
<html lang="en">
<head>
<meta charset="utf-8">
<title>Thornfield Marsh, LLC – Lawyers</title>
<link rel="stylesheet" href="https://fonts.googleapis.com/css2?family=Mulish:ital,wght@0,400;0,600;0,700;1,600&family=Roboto+Condensed:wght@400&display=swap">
<style>
:root{
  --navy:#0c1a86;
  --navy-dark:#061060;
  --blue:#0677BA;
  --bright:#1c8fe3;
  --sky:#7BADD7;
  --pale:#CADEEF;
  --mist:#E8F1F8;
  --gold:#C9A227;
  --gold-soft:#E9D89A;
  --gray-bg:#f5f5f5;
  --ink:#222;
  --line:#e2e2e2;
}
*{box-sizing:border-box;margin:0;padding:0}
html,body{width:1200px;height:4184px;overflow:hidden}
body{font-family:"Mulish",sans-serif;color:var(--ink);background:#fff;font-size:12px;line-height:1.9}
section,header,footer{position:relative;width:1200px}
.section-title{position:absolute;left:0;width:1200px;text-align:center;font-size:36px;font-weight:400;color:#222;letter-spacing:.5px;line-height:1.2}
.title-rule{position:absolute;left:570px;width:60px;height:3px;display:flex;gap:6px}
.title-rule span{flex:1;background:var(--navy)}
.title-rule span:nth-child(2){background:var(--gold)}
.btn{position:absolute;display:flex;align-items:center;height:36px;border:2px solid var(--navy);background:#fff;color:var(--bright);font-size:14px;font-weight:600;padding-right:12px;white-space:nowrap}
.btn .mark{width:34px;height:32px;background:var(--navy);margin-right:9px;position:relative}
.btn .mark::after{content:"";position:absolute;left:11px;top:10px;width:12px;height:12px;background:var(--gold)}
.btn::after{content:"»";position:absolute;right:8px;bottom:-13px;font-size:13px;color:var(--gold);background:#fff;line-height:1;padding:0 2px}
.brand{display:flex;align-items:center;gap:12px;border:4px solid var(--navy);background:#fff;padding:0 16px 0 0;height:62px}
.brand .sq{width:54px;height:54px;background:var(--gold)}
.brand .name{font-size:26px;font-weight:700;color:var(--navy);letter-spacing:.5px;white-space:nowrap}
.ph{position:absolute}
.tick{display:flex;gap:10px;margin-top:4px}
.tick svg{flex:none;margin-top:4px}

/* header */
.site-header{height:98px;border-bottom:3px solid var(--gold)}
.site-header .brand{position:absolute;left:142px;top:16px}
.call{position:absolute;left:882px;top:10px;display:flex;gap:10px;align-items:center}
.call .ico{width:32px;height:32px;background:var(--navy);display:flex;align-items:center;justify-content:center}
.call small{display:block;font-size:11px;color:#555;line-height:1.2}
.call b{font-size:19px;color:#111;line-height:1.1}
.nav{position:absolute;right:142px;top:64px;display:flex;gap:31px;font-size:12px;font-weight:600;color:#222}
.nav .on{color:var(--navy);border-bottom:2px solid var(--gold)}

/* hero */
.hero{height:527px;color:#fff}
.hero-bg{position:absolute;inset:0;background:radial-gradient(circle at 74% 45%,#1e5a94 0%,#0b2a4e 35%,#06182e 70%,#030c18 100%)}
.hero h1{position:absolute;left:142px;top:160px;font-family:"Roboto Condensed",sans-serif;font-weight:400;font-size:40px;color:var(--bright);letter-spacing:.3px;line-height:1.2}
.hero p{position:absolute;left:142px;top:218px;width:365px;font-size:14px;line-height:27px}
.hero .btn{left:142px;top:317px;color:#fff;background:transparent;border-color:var(--gold)}
.hero .btn::after{background:transparent}

/* attorneys */
.attorneys{height:617px}
.attorneys .lead{position:absolute;left:155px;top:134px;width:890px;text-align:center;font-size:14px;line-height:24px;color:#222}
.person{position:absolute;left:142px;width:302px;height:72px;display:flex;align-items:center;gap:18px;padding-left:12px}
.person.active{border:1.5px solid var(--sky);border-left:4px solid var(--gold);border-radius:4px;box-shadow:0 2px 8px rgba(0,84,170,.12)}
.avatar{width:48px;height:48px;border-radius:50%;background:linear-gradient(#c9c9c9,#8a8f99)}
.person b{display:block;font-size:17px;font-weight:700;color:#111;line-height:1.2}
.person.active b{color:var(--navy)}
.person span{font-size:13px;color:#333;line-height:1.3}
.person.active span{color:var(--navy)}
.attorneys .tag{position:absolute;left:142px;top:508px;font-size:22px;font-weight:700;color:var(--navy);line-height:1.3}
.bio{position:absolute;left:766px;top:218px;width:295px}
.bio h3{font-size:17px;font-weight:700;color:var(--navy);line-height:1.3}
.bio h3 small{font-size:13px;font-weight:600;color:var(--gold)}
.bio .hl{color:var(--bright);font-size:12px;line-height:23px;margin-top:10px}
.bio .tx{font-size:12px;line-height:23px;color:#222}

/* blog */
.blog{height:710px;background:var(--gray-bg)}
.card{position:absolute;background:#fff;border:1px solid var(--line)}
.card h4{font-size:15px;font-weight:700;color:var(--navy);line-height:22px}
.card .by{font-size:11px;color:var(--gold);font-weight:700}
.card p{font-size:12px;line-height:23px;color:#222}
.big h4{margin:18px 20px 4px}
.big p{margin:0 20px}
.big hr{border:0;border-top:1px solid var(--line);margin:8px 20px 6px}
.big .by{margin-left:20px}
.small .ph{left:6px;top:6px;width:142px;bottom:6px}
.small .body{position:absolute;left:164px;top:22px;right:14px}
.small h4{font-size:12px;line-height:18px}
.small p{margin-top:6px}
.small .by{margin-top:8px;display:block}

/* litigation */
.litigation{height:1050px}
.lit-text{position:absolute;width:470px;font-size:12px;line-height:23px;color:#222}
.lit-text h3{font-size:17px;font-weight:700;color:var(--navy);margin-bottom:8px;line-height:1.3}

/* step */
.step{height:585px;background:var(--gray-bg)}
.step h2{position:absolute;left:475px;top:94px;font-size:36px;font-weight:400;color:#222;line-height:1.2;letter-spacing:.3px}
.step .title-rule{left:475px;top:145px}
.step h5{position:absolute;left:475px;top:170px;font-size:15px;font-weight:700;color:#111;line-height:1.3}
.step .intro{position:absolute;left:475px;top:200px;width:520px;font-size:11.5px;line-height:19px}
.contact-row{position:absolute;left:475px;display:flex;gap:14px;align-items:center;font-size:14px;color:#111}
.dash{position:absolute;left:475px;width:372px;border-top:1px dashed var(--gold)}
.ghost{position:absolute;left:475px;top:444px;font-family:"Roboto Condensed",sans-serif;font-size:58px;color:var(--mist);line-height:1;white-space:nowrap}

/* message */
.message{height:550px}
.message .brand{position:absolute;left:182px;top:170px}
.office{position:absolute;left:182px;top:254px;width:400px;font-size:11.5px;line-height:21px}
.office b{color:var(--navy)}
.slogan{position:absolute;left:178px;top:366px;width:420px;font-size:18px;font-style:italic;font-weight:600;color:var(--gold);line-height:31px}
.field{position:absolute;left:673px;width:348px;height:40px;border:1px solid #eee;border-radius:3px;display:flex;align-items:center;gap:10px;padding-left:12px;font-size:12px;color:#333;background:#fff}
.field.area{height:70px;align-items:flex-start;padding-top:10px}
.disclaimer{position:absolute;left:150px;top:468px;width:900px;text-align:center;font-size:10px;line-height:18px;color:#222}
.disclaimer b{color:var(--navy)}
.site-footer{height:44px;background:var(--navy-dark);color:#fff;text-align:center;font-size:11px;line-height:41px;border-top:3px solid var(--gold)}
</style>
</head>
<body>

<header class="site-header">
  <div class="brand"><div class="sq"></div><span class="name">THORNFIELD MARSH, LLC</span></div>
  <div class="call">
    <div class="ico"><svg width="16" height="16" viewBox="0 0 24 24" fill="none" stroke="#C9A227" stroke-width="2"><path d="M22 16.9v3a2 2 0 0 1-2.2 2 19.8 19.8 0 0 1-8.6-3.1 19.5 19.5 0 0 1-6-6A19.8 19.8 0 0 1 2.1 4.2 2 2 0 0 1 4.1 2h3a2 2 0 0 1 2 1.7c.1 1 .4 1.9.7 2.8a2 2 0 0 1-.5 2.1L8 9.9a16 16 0 0 0 6 6l1.3-1.3a2 2 0 0 1 2.1-.4c.9.3 1.8.6 2.8.7a2 2 0 0 1 1.7 2z"/></svg></div>
    <div><small>Call Us Today</small><b>555.210.4477</b></div>
  </div>
  <nav class="nav"><span class="on">Home</span><span>About Us</span><span>Blog</span><span>MDLs and Class Actions</span><span>Contact Us</span></nav>
</header>

<section class="hero">
  <div class="hero-bg" role="img" aria-label="Night city skyline with glowing legal icons: scales of justice, courthouse, gavel, documents and globe"></div>
  <h1>A Multi-Service Law Firm</h1>
  <p>Our Attorneys Pride Ourselves On Being Accessible To Our Clients And Providing Exceptional Value For The Legal Services Rendered.</p>
  <div class="btn"><span class="mark"></span>Free Consultation</div>
</section>

<section class="attorneys">
  <h2 class="section-title" style="top:68px">Meet Our Attorneys</h2>
  <div class="title-rule" style="top:118px"><span></span><span></span><span></span></div>
  <p class="lead">Consequat vel illum dolore eu feugiat nulla facilisis at vero eros et accumsan et iusto odio dignissim qui blandit praesent luptatum zzril delenit augue duis dolore te feugait nulla facilisi.</p>

  <div class="person active" style="top:212px"><div class="avatar" role="img" aria-label="Portrait of Brent Marsh"></div><div><b>Brent Marsh</b><span>Attorney</span></div></div>
  <div class="person" style="top:312px"><div class="avatar" role="img" aria-label="Portrait of Leonard Thornfield"></div><div><b>Leonard Thornfield</b><span>Attorney</span></div></div>
  <div class="person" style="top:412px"><div class="avatar" role="img" aria-label="Portrait of Melinda Carrow"></div><div><b>Melinda Carrow</b><span>Legal Assistant</span></div></div>
  <div class="tag">A Multi-Service Law Firm</div>

  <div class="ph" role="img" aria-label="Photo of attorney Brent Marsh in a suit" style="left:474px;top:212px;width:266px;height:331px;background:linear-gradient(180deg,#e3e3e3,#b9bcc2 60%,#2c3550)"></div>

  <div class="bio">
    <h3>Brent Marsh, <small>Attorney</small></h3>
    <p class="hl">Brent Marsh helps people reclaim their voices and protect their rights, providing consumer debt defense, criminal defense, and insurance litigation.</p>
    <p class="tx">consequat, vel illum dolore eu feugiat nulla facilisis at vero erconsequat, vel illum dolore eu feugiat nulla facilisis at vero eros et accumsan et iusto odio dignissim qui blandit praesrent luptatum zzril delenit augue duis do raesreent luptatum zzril delenit augue duis.</p>
  </div>
  <div class="btn" style="left:766px;top:504px"><span class="mark"></span>Contact Us</div>
</section>

<section class="blog">
  <h2 class="section-title" style="top:78px">Latest Blog &amp; Video Posts</h2>
  <div class="title-rule" style="top:128px"><span></span><span></span><span></span></div>

  <article class="card big" style="left:142px;top:158px;width:446px;height:390px">
    <div class="ph" role="img" aria-label="Video still: people reviewing and signing a document at a desk" style="position:relative;margin:6px;height:202px;background:linear-gradient(135deg,#6b5a47,#c8b59a 55%,#e6ddd0)"></div>
    <h4>Consequat, Vel Illum Dolore Eu Feugiat Nulla Facilisis At Vero Eros Et Accumsan</h4>
    <p>Consequat, vel illum dolore eu feugiat nulla facilisis at vero eros et accumsan et iusto odio dignissim qui blandit praesent luptatum zzril delenit augue duis dolore te feugait nulla facilisi.</p>
    <hr><span class="by">By Admin</span>
  </article>

  <article class="card small" style="left:612px;top:158px;width:446px;height:178px">
    <div class="ph" role="img" aria-label="Lawyers meeting with a client in an office" style="background:linear-gradient(135deg,#5f6b78,#c3c8cd)"></div>
    <div class="body"><h4>Et Iusto Odio Dignissim Qui Bndit Praesent Luptatum Zzril Delenit Augue.</h4><p>Consequat, vel illum dolore eu feugiat nulla facilisis at vero eros et accumsan et iusto odio dignissim qui blandit.</p><span class="by">By Admin</span></div>
  </article>

  <article class="card small" style="left:612px;top:367px;width:446px;height:185px">
    <div class="ph" role="img" aria-label="Lawyer holding a tablet beside courthouse columns" style="background:linear-gradient(90deg,#9aa3ad,#dde1e4 50%,#8c96a1)"></div>
    <div class="body"><h4>Et Iusto Odio Dignissim Qui Bndit Praesent Luptatum Zzril Delenit Augue.</h4><p>Consequat, vel illum dolore eu feugiat nulla facilisis at vero eros et accumsan et iusto odio dignissim qui blandit.</p><span class="by">By Admin</span></div>
  </article>

  <div class="btn" style="left:535px;top:595px"><span class="mark"></span>Contact Us</div>
</section>

<section class="litigation">
  <h2 class="section-title" style="top:75px">Multi District Litigation and Class Actions</h2>
  <div class="title-rule" style="top:125px"><span></span><span></span><span></span></div>

  <div class="ph" role="img" aria-label="Bronze statue of Lady Justice with a gavel and books on a desk" style="left:142px;top:165px;width:398px;height:370px;background:linear-gradient(135deg,#2d2a26,#6b5638 55%,#a98a5c)"></div>
  <div class="lit-text" style="left:592px;top:165px">
    <h3>Multi District Litigation</h3>
    <p>Ut wisi enim ad minim veniam, quis nostrud exerci tation ullamcorper lore uscipit lobortis nisl ut aliquip ex ea commodo consequat. Ut wisi enim ad minim veniam, quis nostrud exerci tation ullamcorper suscipit lobortis nisl ut aliquip ex ea commodo consequat. Ut wisi enim ad minim veniam, quis nostrud exerci tation ullamcorper suscipit lobortis nisl ut aliquip ex ea commodo consequat.</p>
    <div class="tick"><svg width="12" height="10" viewBox="0 0 12 10"><path d="M1 5l3.5 3.5L11 1" fill="none" stroke="#C9A227" stroke-width="1.8"/></svg><span>Consequat, vel illum dolore eu feugiat nulla facilisis at vero eros</span></div>
    <div class="tick"><svg width="12" height="10" viewBox="0 0 12 10"><path d="M1 5l3.5 3.5L11 1" fill="none" stroke="#C9A227" stroke-width="1.8"/></svg><span>Ut wisi enim ad minim veniam, quis nostxerci tation ullamcorper lore uscipit lobortis nisl ut aliquip.</span></div>
    <div class="tick"><svg width="12" height="10" viewBox="0 0 12 10"><path d="M1 5l3.5 3.5L11 1" fill="none" stroke="#C9A227" stroke-width="1.8"/></svg><span>Consequat, vel illum dolore eu feugiat nulla facilisis at vero eros</span></div>
    <div class="tick"><svg width="12" height="10" viewBox="0 0 12 10"><path d="M1 5l3.5 3.5L11 1" fill="none" stroke="#C9A227" stroke-width="1.8"/></svg><span>Ut wisi enim ad minim veniam, quis nostxerci tation ullamcorper lore uscipit lobortis nisl ut aliquip.</span></div>
  </div>
  <div class="btn" style="left:594px;top:493px"><span class="mark"></span>Contact Us</div>

  <div class="lit-text" style="left:142px;top:607px">
    <h3>Class Action</h3>
    <p>Ut wisi enim ad minim veniam, quis nostrud exerci tation ullamcorper lore uscipit lobortis nisl ut aliquip ex ea commodo consequat. Ut wisi enim ad minim veniam, quis nostrud exerci tation ullamcorper suscipit lobortis nisl ut aliquip ex ea commodo consequat. Ut wisi enim ad minim veniam, quis nostrud exerci tation ullamcorper suscipit lobortis nisl ut aliquip ex ea commodo consequat.</p>
    <div class="tick"><svg width="12" height="10" viewBox="0 0 12 10"><path d="M1 5l3.5 3.5L11 1" fill="none" stroke="#C9A227" stroke-width="1.8"/></svg><span>Consequat, vel illum dolore eu feugiat nulla facilisis at vero eros</span></div>
    <div class="tick"><svg width="12" height="10" viewBox="0 0 12 10"><path d="M1 5l3.5 3.5L11 1" fill="none" stroke="#C9A227" stroke-width="1.8"/></svg><span>Ut wisi enim ad minim veniam, quis nostxerci tation ullamcorper lore uscipit lobortis nisl ut aliquip.</span></div>
    <div class="tick"><svg width="12" height="10" viewBox="0 0 12 10"><path d="M1 5l3.5 3.5L11 1" fill="none" stroke="#C9A227" stroke-width="1.8"/></svg><span>Consequat, vel illum dolore eu feugiat nulla facilisis at vero eros</span></div>
    <div class="tick"><svg width="12" height="10" viewBox="0 0 12 10"><path d="M1 5l3.5 3.5L11 1" fill="none" stroke="#C9A227" stroke-width="1.8"/></svg><span>Ut wisi enim ad minim veniam, quis nostxerci tation ullamcorper lore uscipit lobortis nisl ut aliquip.</span></div>
  </div>
  <div class="btn" style="left:144px;top:933px"><span class="mark"></span>Contact Us</div>

  <div class="ph" role="img" aria-label="Hand above a keyboard with glowing icons of scales, courthouse, book and gavel" style="left:660px;top:603px;width:398px;height:372px;background:radial-gradient(circle at 55% 40%,#7fb3e8,#2c63a8 45%,#123466)"></div>
</section>

<section class="step">
  <div class="ph" role="img" aria-label="Illustration of a man in a blue jacket pointing toward the text" style="left:200px;top:80px;width:240px;height:470px;background:linear-gradient(180deg,#f5f5f5,#d8e4f2 40%,#9cc0e6)"></div>
  <h2>Take the First Step Toward Justice</h2>
  <div class="title-rule"><span></span><span></span><span></span></div>
  <h5>Let Us Fight for the Multi District Litigation and Class Actions</h5>
  <p class="intro">Ut wisi enim ad minim veniam, quis nostxerci tation ullamcorper lore uscipit lobortis nisl ut aliquip.Ut wisi enim ad minim veniam.</p>
  <div class="contact-row" style="top:254px"><svg width="24" height="24" viewBox="0 0 24 24" fill="none" stroke="#0c1a86" stroke-width="1.5"><path d="M22 16.9v3a2 2 0 0 1-2.2 2 19.8 19.8 0 0 1-8.6-3.1 19.5 19.5 0 0 1-6-6A19.8 19.8 0 0 1 2.1 4.2 2 2 0 0 1 4.1 2h3a2 2 0 0 1 2 1.7c.1 1 .4 1.9.7 2.8a2 2 0 0 1-.5 2.1L8 9.9a16 16 0 0 0 6 6l1.3-1.3a2 2 0 0 1 2.1-.4c.9.3 1.8.6 2.8.7a2 2 0 0 1 1.7 2z"/></svg>Call now: 555.210.4477</div>
  <div class="dash" style="top:290px"></div>
  <div class="contact-row" style="top:309px"><svg width="24" height="22" viewBox="0 0 24 22" fill="none" stroke="#0c1a86" stroke-width="1.5"><rect x="2" y="5" width="20" height="14" rx="1"/><path d="M2 6l10 7 10-7"/></svg>Email: inquiry@thornfieldmarshlaw.com</div>
  <div class="dash" style="top:345px"></div>
  <div class="contact-row" style="top:369px"><svg width="22" height="24" viewBox="0 0 22 24" fill="none" stroke="#0c1a86" stroke-width="1.5"><path d="M11 22s7-7 7-12a7 7 0 0 0-14 0c0 5 7 12 7 12z"/><circle cx="11" cy="10" r="2.5"/></svg>Visit: 214 Harbor Ave., Bayport, AL 36690</div>
  <div class="ghost">Call Now: 555.210.4477</div>
</section>

<section class="message">
  <h2 class="section-title" style="top:73px">Leave Us A Message</h2>
  <div class="title-rule" style="top:123px"><span></span><span></span><span></span></div>

  <div class="brand"><div class="sq"></div><span class="name">THORNFIELD MARSH, LLC</span></div>
  <p class="office"><b>The Ashcombe Law Firm, is located in Coral Bay, FL.</b><br>We serve Palm Beach County, Miami Dade County, Broward County, Martin County, St. Lucie County, Okeechobee County, Lee County and the surrounding areas.</p>
  <p class="slogan">Navigating Legal Challenges with Expertise and Care.</p>

  <div class="field" style="top:170px"><svg width="14" height="14" viewBox="0 0 24 24" fill="none" stroke="#0c1a86" stroke-width="2"><circle cx="12" cy="8" r="4"/><path d="M4 22c0-4 4-7 8-7s8 3 8 7"/></svg>Your Name*</div>
  <div class="field" style="top:215px"><svg width="14" height="14" viewBox="0 0 24 24" fill="none" stroke="#0c1a86" stroke-width="2"><rect x="2" y="5" width="20" height="14"/><path d="M2 6l10 7 10-7"/></svg>Your Email*</div>
  <div class="field" style="top:260px"><svg width="14" height="14" viewBox="0 0 24 24" fill="none" stroke="#0c1a86" stroke-width="2"><path d="M22 16.9v3a2 2 0 0 1-2.2 2A19.8 19.8 0 0 1 2.1 4.2 2 2 0 0 1 4.1 2h3a2 2 0 0 1 2 1.7l.7 2.8-1.8 3.4a16 16 0 0 0 6 6l3.4-1.8 2.8.7a2 2 0 0 1 1.7 2z"/></svg>Your Phone*</div>
  <div class="field area" style="top:305px"><svg width="14" height="14" viewBox="0 0 24 24" fill="none" stroke="#0c1a86" stroke-width="2"><path d="M21 12a8 8 0 0 1-12 7l-5 2 2-5a8 8 0 1 1 15-4z"/></svg>Message*</div>
  <div class="btn" style="left:677px;top:394px"><span class="mark"></span>Send Message</div>

  <p class="disclaimer"><b>Disclaimer :</b> No representation is made that the quality of the legal services to be performed is greater than the quality of legal services performed by other lawyers. Please do not include any confidential or sensitive information in a contact form, text message, or voicemail. The contact form sends information by non-encrypted email, which is not secure. Submitting a contact form, sending a text message, making a phone call, or leaving a voicemail does not create an attorney-client relationship.</p>
</section>

<footer class="site-footer">© 2025. Thornfield Marsh, LLC Lawyers. All Rights Reserved</footer>

</body>
</html>
```